blue ridge cooling & vent company flyer for listbarnet ad

size should be 1200x900
this is an ac company, we have a logo but not necessary to use
we offer free estimates, we are open 24/7, fast and affordable
service, licensed and insured
we sell all brands and service all
we offer services for refrigeration residential and commercial
I will post a few of my ads I made but need a pros idea

Blue Ridge Cooling & Vent Company
555-318-2746
blueridgevent@mailpost.example
blueridgevent247.example
license # must be on flyer state law it is CAC5273614
if you use the logo please remove the building

Target Market(s)

any one who needs has an ac in home

Industry/Entity Type

Hvac

Requirements
Must have
• contact info must be big

```html
<!DOCTYPE html>
<html lang="en">
<head>
<meta charset="utf-8">
<title>Blue Ridge Cooling &amp; Vent Company – Flyer</title>
<link rel="stylesheet" href="https://fonts.googleapis.com/css2?family=Oswald:wght@500;600&family=Lato:ital,wght@0,700;0,900;1,700&display=swap">
<style>
  :root {
    --navy: #2b3086;
    --red: #d3212a;
    --ink: #262626;
    --grey-band: #dcdcdc;
    --paper: #ffffff;
    --unit-dark: #3a3d3c;
    --unit-mid: #5c605e;
  }
  * { margin: 0; padding: 0; box-sizing: border-box; }
  html, body { width: 1200px; height: 902px; overflow: hidden; background: #ececec; }
  .flyer {
    position: relative; width: 1200px; height: 902px; overflow: hidden;
    background: linear-gradient(160deg, #ffffff 0%, #f4f4f6 60%, #e9e9ee 100%);
    font-family: "Lato", sans-serif;
  }
  .backdrop { position: absolute; inset: 0; }
  .header {
    position: absolute; left: 0; top: 0; width: 1200px; height: 122px;
    display: flex; align-items: center; justify-content: center;
    font-family: "Oswald", sans-serif; font-weight: 500; font-size: 50px;
    letter-spacing: -0.5px; color: var(--navy); text-transform: uppercase;
  }
  .header .accent { color: var(--red); margin-left: 12px; }
  .headline {
    position: absolute; left: 40px; top: 152px;
    font-family: "Oswald", sans-serif; font-weight: 500; font-size: 62px;
    letter-spacing: -0.5px; line-height: 1; color: #3b3b3b; text-transform: uppercase;
    white-space: nowrap;
  }
  .headline .accent { color: var(--red); }
  .benefits { position: absolute; left: 52px; top: 247px; list-style: none; }
  .benefits li {
    display: flex; align-items: center; height: 50px;
    font-style: italic; font-weight: 700; font-size: 29px; color: var(--ink);
  }
  .benefits li::before {
    content: ""; width: 20px; height: 20px; border-radius: 50%;
    background: var(--navy); margin-right: 22px;
  }
  .services {
    position: absolute; left: -4px; top: 408px; width: 590px; height: 113px;
    border: 4px solid var(--navy); border-left: none;
    border-radius: 0 50px 50px 0; background: var(--paper);
    padding: 20px 0 0 44px;
  }
  .services h2 { font-style: italic; font-weight: 700; font-size: 33px; color: var(--red); }
  .services .sectors { display: flex; gap: 56px; margin-top: 10px; }
  .services .sectors span {
    display: flex; align-items: center; gap: 26px;
    font-style: italic; font-weight: 700; font-size: 27px; color: var(--ink);
  }
  .phone {
    position: absolute; left: 34px; top: 560px; display: flex; align-items: center; gap: 22px;
    font-family: "Oswald", sans-serif; font-weight: 600; font-size: 86px; color: #1e1e1e; line-height: 1;
  }
  .license {
    position: absolute; left: 180px; top: 683px; width: 356px; height: 40px;
    display: flex; align-items: center; justify-content: center;
    font-weight: 900; font-size: 25px; color: #fff;
  }
  .contacts { position: absolute; left: 52px; top: 768px; list-style: none; }
  .contacts li {
    display: flex; align-items: center; gap: 20px; height: 50px;
    font-weight: 900; font-size: 28px; color: #fff;
  }
  .open-badge { position: absolute; left: 746px; top: 138px; width: 440px; height: 160px; }
  .open-badge .pill {
    position: absolute; left: 0; top: 26px; width: 320px; height: 101px;
    border-radius: 50px; background: var(--navy);
    display: flex; align-items: center; padding-left: 26px;
    font-style: italic; font-weight: 700; font-size: 39px; color: #fff;
    box-shadow: 0 4px 8px rgba(0,0,0,.25);
  }
  .open-badge .clock { position: absolute; left: 277px; top: 0; }
  .product-photo {
    position: absolute; left: 667px; top: 360px; width: 503px; height: 493px;
    background: linear-gradient(180deg, var(--unit-mid) 0%, var(--unit-dark) 100%);
    border-radius: 6px;
  }
</style>
</head>
<body>
<main class="flyer">
  <svg class="backdrop" width="1200" height="902" viewBox="0 0 1200 902" aria-hidden="true">
    <path d="M0 0 H1200 V100 Q1185 124 1140 126 H60 Q15 124 0 100 Z" fill="#f1f1f3"/>
    <path d="M0 104 Q15 126 60 128 H1140 Q1185 126 1200 104" fill="none" stroke="#cfcfd4" stroke-width="3"/>
    <path d="M1200 470 L620 620 L620 902 L1200 902 Z" fill="var(--navy)"/>
    <path d="M1200 448 L640 590 L640 604 L1200 466 Z" fill="var(--red)"/>
    <path d="M0 736 Q300 720 700 735 L700 902 L0 902 Z" fill="var(--navy)"/>
    <path d="M0 706 Q320 740 760 728 L760 746 Q320 758 0 738 Z" fill="var(--grey-band)"/>
    <path d="M0 686 Q300 716 740 700 L740 706 Q300 724 0 696 Z" fill="var(--red)"/>
    <rect x="180" y="683" width="356" height="40" rx="20" fill="var(--red)"/>
  </svg>

  <header class="header">Blue Ridge Cooling <span class="accent">&amp; Vent Company</span></header>

  <h1 class="headline"><span class="accent">We offer</span> free estimates</h1>

  <ul class="benefits">
    <li>Fast and affordable service</li>
    <li>Licensed and insured</li>
    <li>We sell all brands and service all</li>
  </ul>

  <section class="services">
    <h2>We offer services for refrigeration</h2>
    <div class="sectors">
      <span><svg width="18" height="18" viewBox="0 0 18 18" aria-hidden="true"><rect x="1" y="3" width="13" height="13" fill="none" stroke="var(--navy)" stroke-width="2"/><path d="M4 9 L8 13 L17 2" fill="none" stroke="var(--navy)" stroke-width="3"/></svg>Residential</span>
      <span><svg width="18" height="18" viewBox="0 0 18 18" aria-hidden="true"><rect x="1" y="3" width="13" height="13" fill="none" stroke="var(--navy)" stroke-width="2"/><path d="M4 9 L8 13 L17 2" fill="none" stroke="var(--navy)" stroke-width="3"/></svg>Commercial</span>
    </div>
  </section>

  <div class="phone">
    <svg width="68" height="68" viewBox="0 0 68 68" aria-hidden="true">
      <circle cx="34" cy="34" r="30" fill="none" stroke="var(--red)" stroke-width="4"/>
      <path d="M24 18 l8 9 -4 5 q4 8 12 12 l5 -4 9 8 -5 6 q-6 3 -16 -4 q-12 -9 -15 -20 q-1 -8 6 -16 z" fill="var(--red)"/>
    </svg>
    555-318-2746
  </div>

  <div class="license">License # CAC5273614</div>

  <ul class="contacts">
    <li><svg width="26" height="24" viewBox="0 0 26 24" aria-hidden="true"><path d="M2 10 L13 2 L24 10 V22 H2 Z" fill="none" stroke="#fff" stroke-width="2"/><path d="M2 10 L13 17 L24 10" fill="none" stroke="#fff" stroke-width="2"/></svg>blueridgevent@mailpost.example</li>
    <li><svg width="26" height="26" viewBox="0 0 26 26" aria-hidden="true"><g fill="none" stroke="#fff" stroke-width="2"><circle cx="13" cy="13" r="11"/><ellipse cx="13" cy="13" rx="5" ry="11"/><path d="M2 13 H24 M4 7 H22 M4 19 H22"/></g></svg>www.blueridgevent247.example</li>
  </ul>

  <div class="open-badge">
    <div class="pill">We are open</div>
    <svg class="clock" width="156" height="156" viewBox="0 0 156 156" aria-hidden="true">
      <circle cx="78" cy="78" r="76" fill="var(--red)"/>
      <circle cx="78" cy="78" r="52" fill="none" stroke="#fff" stroke-width="5"/>
      <path d="M78 22 V34 M78 122 V134 M22 78 H34 M122 78 H134" stroke="var(--red)" stroke-width="8"/>
      <path d="M78 24 V32 M78 124 V132 M24 78 H32 M124 78 H132" stroke="#fff" stroke-width="4"/>
      <text x="78" y="88" text-anchor="middle" font-family="Lato, sans-serif" font-weight="900" font-size="27" fill="#fff">24/7</text>
    </svg>
  </div>

  <div class="product-photo" role="img" aria-label="Photo of an outdoor air conditioning condenser unit beside a tall indoor air handler cabinet"></div>
</main>
</body>
</html>
```